Pet Care Business Card

Dog & Cat Grooming, we come to you or come to Whisker Haven Gympie
Doggy day care,
Boutique holiday care,
Pet Supplies
All Natural Products used
Have created the logo, which I will forward shortly but need help to have it on flyers business cards ect
email whiskerhavengympie@lumomail.test
Ph: 0417265531
Colours: Green Black and paws prints nott sure what colour for them
Thank you to all that forwarded their designs, very hard choice and I thank you for your effort, shall recommend this to all my collegues
Thanks Again Tess :)
Business
0417265531
57 upper Wendlock Road
Brindale QLD 4570

```html
<!DOCTYPE html>
<html lang="en">
<head>
<meta charset="utf-8">
<title>Whisker Haven Brindale – Business Card</title>
<link href="https://fonts.googleapis.com/css2?family=Alegreya:wght@700&family=Exo+2:wght@400;500&display=swap" rel="stylesheet">
<style>
  :root {
    --page: #d8d3cd;
    --card: #f1efec;
    --card-edge: #e2ded9;
    --band: #9b4a10;
    --band-trim: #d6a07a;
    --brand: #9b4a10;
    --ink-light: #ffffff;
  }
  html, body {
    margin: 0;
    padding: 0;
    width: 1200px;
    height: 769px;
    overflow: hidden;
    background: var(--page);
  }
  .card {
    position: absolute;
    left: 100px;
    top: 97px;
    width: 1000px;
    height: 575px;
    border-radius: 26px;
    overflow: hidden;
    background: linear-gradient(180deg, var(--card) 0%, #f6f4f2 50%, var(--card-edge) 100%);
    box-shadow: 0 10px 30px rgba(0,0,0,0.12);
  }
  .card-shapes {
    position: absolute;
    inset: 0;
  }
  .brand-mark {
    position: absolute;
    left: 420px;
    top: 27px;
    width: 160px;
    height: 160px;
  }
  .brand-name {
    position: absolute;
    left: 0;
    width: 1000px;
    top: 198px;
    margin: 0;
    text-align: center;
    font-family: "Alegreya", Georgia, serif;
    font-weight: 700;
    font-size: 42px;
    color: var(--brand);
    line-height: 1;
  }
  .person {
    position: absolute;
    left: 68px;
    width: 400px;
    top: 344px;
    text-align: center;
    color: var(--ink-light);
    font-family: "Exo 2", Arial, sans-serif;
  }
  .person-name {
    margin: 0;
    font-size: 27px;
    font-weight: 500;
    letter-spacing: 1.5px;
    line-height: 1.2;
  }
  .person-role {
    margin: 6px 0 0;
    font-size: 21px;
    font-weight: 400;
    letter-spacing: 0.5px;
  }
  .divider {
    position: absolute;
    left: 499px;
    top: 290px;
    width: 2px;
    height: 179px;
    background: var(--ink-light);
  }
  .contacts {
    position: absolute;
    left: 576px;
    top: 304px;
    margin: 0;
    padding: 0;
    list-style: none;
    font-family: "Exo 2", Arial, sans-serif;
    font-size: 16.5px;
    color: var(--ink-light);
    letter-spacing: 0.6px;
  }
  .contacts li {
    display: flex;
    align-items: center;
    height: 30.5px;
    white-space: nowrap;
  }
  .contacts svg {
    width: 19px;
    height: 19px;
    margin-right: 10px;
    flex: none;
  }
</style>
</head>
<body>
  <div class="card">
    <svg class="card-shapes" viewBox="0 0 1000 575" aria-hidden="true">
      <path d="M0,221 Q500,309 1000,221" fill="none" stroke="var(--band-trim)" stroke-width="8"/>
      <path d="M0,230 Q500,322 1000,230 L1000,525 Q500,459 0,525 Z" fill="var(--band)"/>
      <path d="M0,539 Q500,467 1000,539" fill="none" stroke="var(--band-trim)" stroke-width="8"/>
    </svg>

    <svg class="brand-mark" viewBox="0 0 160 160" aria-hidden="true">
      <circle cx="80" cy="80" r="74" fill="none" stroke="var(--brand)" stroke-width="8"/>
    </svg>
    <h1 class="brand-name">Whisker Haven Brindale</h1>

    <div class="person">
      <p class="person-name">ROWAN PIKE</p>
      <p class="person-role">Managing Director</p>
    </div>

    <div class="divider"></div>

    <ul class="contacts">
      <li>
        <svg viewBox="0 0 20 20"><circle cx="10" cy="10" r="10" fill="#fff"/><path d="M6.5 5.5 l2 -0.5 l1.2 2.6 l-1.3 1 q0.9 2 2.9 3 l1 -1.3 l2.6 1.2 l-0.5 2 q-5 0.5 -7.9 -8z" fill="var(--band)"/></svg>
        040 817 2956
      </li>
      <li>
        <svg viewBox="0 0 20 20"><circle cx="10" cy="10" r="10" fill="#fff"/><rect x="6.8" y="4" width="6.4" height="12" rx="1.2" fill="var(--band)"/><rect x="7.9" y="5.5" width="4.2" height="7.5" fill="#fff"/></svg>
        073 604 1182
      </li>
      <li>
        <svg viewBox="0 0 20 20"><circle cx="10" cy="10" r="10" fill="#fff"/><rect x="5" y="6.5" width="10" height="7" rx="0.8" fill="var(--band)"/><path d="M5.5 7 L10 10.5 L14.5 7" fill="none" stroke="#fff" stroke-width="1"/></svg>
        yourname@mail.test
      </li>
      <li>
        <svg viewBox="0 0 20 20"><circle cx="10" cy="10" r="10" fill="#fff"/><g fill="none" stroke="var(--band)" stroke-width="1.2"><circle cx="10" cy="10" r="5.5"/><ellipse cx="10" cy="10" rx="2.4" ry="5.5"/><path d="M4.5 10 H15.5 M5.3 7.3 H14.7 M5.3 12.7 H14.7"/></g></svg>
        www.yourwebsite.test
      </li>
      <li>
        <svg viewBox="0 0 20 20"><circle cx="10" cy="10" r="10" fill="#fff"/><path d="M10 16 Q5.5 10.5 5.5 8.3 A4.5 4.5 0 0 1 14.5 8.3 Q14.5 10.5 10 16z" fill="var(--band)"/><circle cx="10" cy="8.3" r="1.7" fill="#fff"/></svg>
        Unit 6, 41 Ferncliff Lane, Brindale QLD
      </li>
    </ul>
  </div>
</body>
</html>
```